Website Design for Chef Varo Chinese Restaurant

Chef Varo is a new Chinese Restaurant. It offers exceptional dining experience with authentic and dynamic dishes created with quality ingredients.

A vivid website theme is required to promote this new restaurant online. Logo, menu, wine list and a few other files are attached for help with designing.

A very rough demo website has been setup and can be accessed via http://www.chefvaro.com.au. It is for telling designers what content is shown up on each page (except for homepage). By reading the about us page, designers can get some more info of Chef Varo. However, the layout, theme color, font, etc are not set in stone. Visitors should be able to feel Chef Varo restaurant's authentic Chinese cuisine and high hygiene standard. Home page of the website could be The "Our website is coming soon" description is shown on demo site but do not required to be presented on new design.

Some main pages design should be included: Home (landing page), About us, Menu (Dishes), Winelist, Gallery, Contact us. No HTML and coding required. The output should be well layered psd or png files with acceptable resolution for web use.

A few other website can be referred to are:

http://belmiraeatery.com.au/
http://www.stone-kettle.com/
http://quillhaven.com.au/
http://meadowbistro.com.au/
http://www.lanternvaledining.com.au/
http://www.thetrove.com.au/

Industry/Entity Type

Restaurant

Requirements
Nice to have
• I expect designs of at least these webpages: homepage, menu page and contact us page. If you can provide "about us" page as well, it will probably help you win the competition. well layered psd or png file is my preference.
Should not have
• You don't have to make html/cs/js or any coding. All I need is just art design

```html
<!DOCTYPE html>
<html lang="en">
<head>
<meta charset="utf-8">
<title>Chef Varo Chinese Restaurant – Menu</title>
<link rel="stylesheet" href="https://fonts.googleapis.com/css2?family=Cabin:wght@400;600;700&display=swap">
<style>
  :root {
    --maroon: #5c1e22;
    --maroon-deep: #4a171a;
    --sand: #a69b6c;
    --sand-side: #a8996b;
    --ink-light: #fbf6e8;
    --rule: #6b1f26;
    --footer: #303030;
    --photo-cream: #eadbc6;
    --photo-bamboo: #c89a62;
    --photo-white: #f7f4ef;
  }
  * { margin: 0; padding: 0; box-sizing: border-box; }
  html, body { width: 1200px; height: 675px; overflow: hidden; background: var(--maroon); }
  body { font-family: "Cabin", Arial, sans-serif; color: var(--ink-light); }

  .canvas {
    position: relative; width: 1200px; height: 675px; overflow: hidden;
    background: radial-gradient(ellipse at 30% 40%, #652428 0%, var(--maroon) 55%, var(--maroon-deep) 100%);
  }

  /* Brand */
  .brand {
    position: absolute; left: 31px; top: 26px; width: 230px; height: 150px;
    display: flex; flex-direction: column; align-items: center; justify-content: center; gap: 14px;
  }
  .brand__mark { width: 40px; height: 40px; background: #d4232b; }
  .brand__name {
    font-weight: 700; font-size: 15px; text-transform: uppercase; color: #ffffff; text-align: center; line-height: 1.25;
  }

  /* Sidebar menu */
  .side-menu {
    position: absolute; left: 26px; top: 200px; width: 238px; height: 326px;
    background: var(--sand-side); box-shadow: 2px 3px 5px rgba(0,0,0,.45);
  }
  .side-menu__title {
    text-align: center; font-weight: 400; font-size: 19px; margin-top: 10px;
  }
  .side-menu__title span { border-bottom: 1px solid var(--ink-light); padding: 0 1px; }
  .side-menu__list { list-style: none; margin: 29px 0 0 30px; width: 199px; font-size: 8px; line-height: 10.55px; }
  .side-menu__list li { display: flex; }
  .side-menu__list .dots { flex: 1; border-bottom: 1px dotted rgba(251,246,232,.8); margin: 0 1px 3px; }

  /* Main panel */
  .panel {
    position: absolute; left: 293px; top: 26px; width: 881px; height: 596px;
    background: var(--sand); box-shadow: 2px 3px 6px rgba(0,0,0,.45);
  }
  .nav {
    position: absolute; right: 42px; top: 15px; font-size: 14px; white-space: nowrap;
  }
  .nav a { color: var(--ink-light); text-decoration: none; }
  .nav a.is-current { font-weight: 700; text-decoration: underline; }
  .nav .sep { margin: 0 3px; }

  .dish-list { position: absolute; left: 43px; top: 43px; width: 187px; }
  .dish { margin-bottom: 24px; }
  .dish__name { text-align: center; font-weight: 400; font-size: 15px; text-transform: uppercase; margin-bottom: 14px; }
  .dish p { font-size: 10px; line-height: 12.7px; text-align: justify; margin-bottom: 12.7px; }
  .dish .label { text-decoration: underline; }

  .divider { position: absolute; left: 260px; top: 46px; width: 1px; height: 525px; background: var(--rule); }
  .divider__knob {
    position: absolute; left: -10px; top: 15px; width: 21px; height: 21px; border-radius: 50%;
    background: var(--rule); border: 2px solid #3c1013;
  }
  .divider__knob::after {
    content: ""; position: absolute; left: 5.5px; top: 5.5px; width: 6px; height: 6px; border-radius: 50%; background: #e8ddc6;
  }

  .gallery { position: absolute; left: 299px; top: 47px; width: 540px; }
  .dish-photo {
    position: absolute; width: 258px; height: 161px; background: #ffffff;
    box-shadow: 3px 3px 5px rgba(0,0,0,.5);
  }
  .dish-photo--framed { padding: 5px; }
  .dish-photo__fill { width: 100%; height: 100%; }
  .fill-basket { background: radial-gradient(ellipse at 50% 45%, var(--photo-bamboo) 0%, #d8b586 35%, var(--photo-cream) 70%); }
  .fill-plate { background: radial-gradient(ellipse at 50% 50%, #d9c9a8 0%, #ece6da 45%, var(--photo-white) 75%); }
  .fill-bun { background: radial-gradient(ellipse at 50% 50%, #e6a13a 0%, #c9955c 40%, #f4efe8 72%); }
  .fill-red { background: radial-gradient(ellipse at 50% 50%, #c9432c 0%, #d89b66 40%, #f7f2ec 72%); }

  .footer {
    position: absolute; left: 0; bottom: 0; width: 1200px; height: 27px;
    background: linear-gradient(#3a3a3a, var(--footer)); display: flex; align-items: center;
    padding: 0 27px; font-size: 11.5px; color: #f2f2f2;
  }
</style>
</head>
<body>
<div class="canvas">

  <header class="brand">
    <div class="brand__mark" aria-hidden="true"></div>
    <div class="brand__name">Chef Varo Chinese Restaurant</div>
  </header>

  <aside class="side-menu">
    <h2 class="side-menu__title"><span>Menu</span></h2>
    <ul class="side-menu__list">
      <li>- Yun Cha<span class="dots"></span>Price</li>
      <li>- Entrée<span class="dots"></span>Price</li>
      <li>- Soup<span class="dots"></span>Price</li>
      <li>- Cold Dishes<span class="dots"></span>Price</li>
      <li>- Seafood Dishes<span class="dots"></span>Price</li>
      <li>- Steak Dishes<span class="dots"></span>Price</li>
      <li>- Chicken Dishes<span class="dots"></span>Price</li>
      <li>- Duck Dishes<span class="dots"></span>Price</li>
      <li>- Lamb Dishes<span class="dots"></span>Price</li>
      <li>- Pork Dishes<span class="dots"></span>Price</li>
      <li>- Tofu Dishes<span class="dots"></span>Price</li>
      <li>- Hot Pot Dishes<span class="dots"></span>Price</li>
      <li>- Vegetable Dishes<span class="dots"></span>Price</li>
      <li>- Special flavour selections<span class="dots"></span>Price</li>
      <li>- Abalone and Sea Cucumber<span class="dots"></span>Price</li>
      <li>- Rice and Noodles<span class="dots"></span>Price</li>
      <li>- Dessert<span class="dots"></span>Price</li>
      <li>- Stew<span class="dots"></span>Price</li>
      <li>- Banquet<span class="dots"></span>Price</li>
      <li>- Wine List<span class="dots"></span>Price</li>
    </ul>
  </aside>

  <main class="panel">
    <nav class="nav">
      <a href="#">Home</a><span class="sep">|</span><a href="#">About Us</a><span class="sep">|</span><a href="#" class="is-current">Menu</a><span class="sep">|</span><a href="#">Wine List</a><span class="sep">|</span><a href="#">Gallery</a><span class="sep">|</span><a href="#">Contact Us</a><span class="sep">|</span><a href="#">Belmira Court</a>
    </nav>

    <section class="dish-list">
      <article class="dish">
        <h3 class="dish__name">Yum Cha</h3>
        <p><span class="label">Description:</span> Lorem ipsum dolor sit amet, consectetur adipisicing elit, sed do eiusmod tempor incididunt ut labore et dolore magna aliqua. Ut enim ad minim veniam, quis nostrud exercitation ullamco laboris nisi ut aliquip ex ea commodo consequat.</p>
        <p><span class="label">Spicy:</span> 1/5</p>
        <p><span class="label">Suggestion:</span> Combine it with wine (example)</p>
        <p><span class="label">Price:</span> XXX</p>
      </article>
      <article class="dish">
        <h3 class="dish__name">Scallop Dumplings</h3>
        <p><span class="label">Description:</span> Lorem ipsum dolor sit amet, consectetur adipisicing elit, sed do eiusmod tempor incididunt ut labore et dolore magna aliqua. Ut enim ad minim veniam, quis nostrud exercitation ullamco laboris nisi ut aliquip ex ea commodo consequat.</p>
        <p><span class="label">Spicy:</span> 1/5</p>
        <p><span class="label">Suggestion:</span> Combine it with wine (example)</p>
        <p><span class="label">Price:</span> XXX</p>
      </article>
    </section>

    <div class="divider"><span class="divider__knob"></span></div>

    <section class="gallery">
      <figure class="dish-photo dish-photo--framed" style="left:0;top:0">
        <div class="dish-photo__fill fill-basket" role="img" aria-label="Photo of prawn dumplings in a bamboo steamer"></div>
      </figure>
      <figure class="dish-photo dish-photo--framed" style="left:281px;top:0">
        <div class="dish-photo__fill fill-basket" role="img" aria-label="Photo of green vegetable dumplings in a bamboo steamer"></div>
      </figure>
      <figure class="dish-photo" style="left:0;top:181px">
        <div class="dish-photo__fill fill-plate" role="img" aria-label="Photo of scallop dumplings on a white plate"></div>
      </figure>
      <figure class="dish-photo" style="left:281px;top:181px">
        <div class="dish-photo__fill fill-plate" role="img" aria-label="Photo of rice noodle rolls with greens on a white plate"></div>
      </figure>
      <figure class="dish-photo" style="left:0;top:363px">
        <div class="dish-photo__fill fill-bun" role="img" aria-label="Photo of golden custard buns in a bamboo steamer"></div>
      </figure>
      <figure class="dish-photo" style="left:281px;top:363px">
        <div class="dish-photo__fill fill-red" role="img" aria-label="Photo of braised chicken feet in a bamboo steamer"></div>
      </figure>
    </section>
  </main>

  <footer class="footer">© 2014 - Chef Varo Chinese Restaurant</footer>
</div>
</body>
</html>
```